Electrical Engineering Business Card Design

I need a business card design for an engineering consulting company based in Orlando, FL. I have had a logo created which the files are attached. We work primarily in the theme park and entertainment market sector but do projects in all market sectors. We have been serving Central Florida since 1994 and continue to strive to serve our clients and provide outstanding designs.
Industry/Entity Type
Theme Park

```html
<!DOCTYPE html>
<html lang="en">
<head>
<meta charset="utf-8">
<title>Voltline Partners – Business Card</title>
<link rel="stylesheet" href="https://fonts.googleapis.com/css2?family=Questrial&display=swap">
<style>
  :root {
    --stage: #e9e9e6;
    --paper: #ffffff;
    --paper-shade: #ececec;
    --green-light: #9ccd4c;
    --green: #82bd3a;
    --green-deep: #5f9a2a;
    --ink-on-green: #ffffff;
    --card-w: 560px;
    --card-h: 320px;
  }
  * { box-sizing: border-box; margin: 0; padding: 0; }
  html, body {
    width: 1200px; height: 800px; overflow: hidden;
    background: var(--stage);
    font-family: "Questrial", "Century Gothic", sans-serif;
  }
  .stage {
    width: 1200px; height: 800px;
    display: flex; flex-direction: column;
    align-items: center; justify-content: center; gap: 50px;
  }
  .card {
    width: var(--card-w); height: var(--card-h);
    display: flex; overflow: hidden;
    box-shadow: 0 4px 14px rgba(0,0,0,.18);
  }
  .panel-white {
    background: linear-gradient(135deg, var(--paper) 0%, var(--paper-shade) 100%);
    display: flex; align-items: center; justify-content: center;
  }
  .panel-green {
    background: linear-gradient(160deg, var(--green-deep) 0%, var(--green) 55%, var(--green-light) 100%);
  }
  .card-front .panel-white { width: 48%; }
  .card-front .panel-green { width: 52%; }
  .card-back .panel-green {
    width: 56%;
    background: linear-gradient(160deg, var(--green-light) 0%, var(--green) 60%, var(--green-deep) 100%);
    color: var(--ink-on-green);
    padding: 92px 0 0 34px;
  }
  .card-back .panel-white { width: 44%; }

  .brand-mark {
    display: flex; align-items: center; gap: 12px;
    color: var(--green);
    font-size: 62px; letter-spacing: 2px; line-height: 1;
  }
  .brand-mark .brand-square {
    width: 22px; height: 22px; background: var(--green);
  }

  .company-name { font-size: 21px; letter-spacing: .5px; margin-bottom: 8px; }
  .contact-list { list-style: none; font-size: 11.5px; line-height: 15px; }
  .contact-list li { display: flex; align-items: flex-start; gap: 8px; }
  .contact-list svg { width: 9px; height: 9px; margin-top: 3px; flex: none; }
  .contact-list .label { width: 78px; flex: none; }
  .contact-list .indent { padding-left: 17px; }
</style>
</head>
<body>
<main class="stage">

  <section class="card card-front" aria-label="Card front">
    <div class="panel-white">
      <div class="brand-mark"><span class="brand-square"></span>VLP</div>
    </div>
    <div class="panel-green"></div>
  </section>

  <section class="card card-back" aria-label="Card back">
    <div class="panel-green">
      <h1 class="company-name">Voltline Partners, PA</h1>
      <ul class="contact-list">
        <li>
          <svg viewBox="0 0 10 10"><path d="M5 0a3.5 3.5 0 0 1 3.5 3.5C8.5 6 5 10 5 10S1.5 6 1.5 3.5A3.5 3.5 0 0 1 5 0z" fill="#fff"/><circle cx="5" cy="3.5" r="1.3" fill="#82bd3a"/></svg>
          <span>PO Box 410278</span>
        </li>
        <li class="indent">Orlando, FL 32805</li>
        <li>
          <svg viewBox="0 0 10 10"><rect x="0" y="2" width="10" height="6.5" fill="#fff"/><path d="M0 2l5 3.5L10 2" stroke="#82bd3a" fill="none"/></svg>
          <span>email: office@voltlinepartners.com</span>
        </li>
        <li>
          <svg viewBox="0 0 10 10"><path d="M2 0.5l2 2.2-1 1.2c.6 1.3 1.7 2.4 3 3l1.2-1 2.2 2-1.2 1.6C4.5 9.2.8 5.5.5 1.7z" fill="#fff"/></svg>
          <span class="label">(phone)</span><span>407-555-0142</span>
        </li>
        <li>
          <svg viewBox="0 0 10 10"><rect x="2.5" y="0.5" width="5" height="3" fill="#fff"/><rect x="0.5" y="3.5" width="9" height="4.5" fill="#fff"/><rect x="2.5" y="6.5" width="5" height="3" fill="#fff" stroke="#82bd3a"/></svg>
          <span class="label">(fax)</span><span>407-555-0198</span>
        </li>
      </ul>
    </div>
    <div class="panel-white">
      <div class="brand-mark"><span class="brand-square"></span>VLP</div>
    </div>
  </section>

</main>
</body>
</html>
```